Feral Horizon, a 3d voxel survival video game needs a card for gaming conventions

I am the lead developer for Feral Horizon http://www.FeralHorizon.example and need a business card to hand out at an indie gaming convention
The card would need to include the game name, website url, my name, position (Lead Developer), e-mail and phone number
The game is a 3d, voxel (with smooth terrain) based survival game with guns and wildlife. The main icon of the game would likely be a grizzly bear but I am willing to accept other designs too.
Attached is a media kit for the game with some images you can use but don't have to its just what little art I can provide. Anything on the website or from the video game can also be used. unrelated art can also be used.
Target Market(s)
Indie Developers/publishers at conferences
Industry/Entity Type
Games
Contact Information for Business Card
Name: Corwin Aldersby
Position: Lead Developer
E-mail: Pale_Lanterns@mailbox.example
Phone number: 555-207-3186

```html
<!DOCTYPE html>
<html lang="en">
<head>
<meta charset="utf-8">
<title>Feral Horizon – Business Card</title>
<link rel="stylesheet" href="https://fonts.googleapis.com/css2?family=Bangers&family=Open+Sans:ital,wght@0,400;1,300&display=swap">
<style>
  :root {
    --page: #ffffff;
    --olive-dark: #4b4f2b;
    --olive-mid: #8a8a73;
    --mist: #e2e1dc;
    --bark: #3d2314;
    --paper: #ffffff;
    --ember: #a3322a;
    --target: #d0202a;
    --fur-dark: #4a2a14;
    --fur-light: #a8693a;
    --ink-light: #ffffff;
    --shadow: rgba(0, 0, 0, 0.28);
  }
  * { margin: 0; padding: 0; box-sizing: border-box; }
  html, body { width: 1200px; height: 1200px; overflow: hidden; background: var(--page); }
  .canvas { position: relative; width: 1200px; height: 1200px; }

  .card {
    position: absolute;
    width: 925px;
    height: 475px;
    border-radius: 22px;
    overflow: hidden;
    box-shadow: 0 6px 10px var(--shadow);
  }

  /* Front */
  .card--front {
    left: 134px; top: 92px;
    background: radial-gradient(ellipse 70% 85% at 62% 78%, var(--mist) 0%, var(--olive-mid) 55%, var(--olive-dark) 100%);
  }
  .front__wordmark {
    position: absolute;
    left: 60px; top: 150px;
    font-family: "Bangers", sans-serif;
    font-size: 120px;
    line-height: 0.95;
    letter-spacing: 4px;
    color: var(--ember);
    text-transform: uppercase;
  }
  .front__wordmark span { display: block; }
  .front__wordmark span + span { padding-left: 110px; }
  .front__bear {
    position: absolute;
    left: 600px; top: 22px;
    width: 325px; height: 350px;
    background: radial-gradient(ellipse 60% 60% at 50% 45%, var(--fur-light) 0%, var(--fur-dark) 70%, rgba(74, 42, 20, 0) 100%);
  }
  .front__target {
    position: absolute;
    left: 697px; top: 187px;
    width: 144px; height: 170px;
  }

  /* Back */
  .card--back {
    left: 140px; top: 645px;
    background: var(--paper);
  }
  .back__band {
    position: absolute;
    left: 0; top: 0;
    width: 100%; height: 320px;
    background: var(--bark);
  }
  .back__name {
    position: absolute;
    left: 94px; top: 34px;
    font-family: "Bangers", sans-serif;
    font-size: 48px;
    letter-spacing: 3px;
    color: var(--ink-light);
    text-transform: uppercase;
  }
  .back__role {
    position: absolute;
    left: 94px; top: 88px;
    font-family: "Open Sans", sans-serif;
    font-style: italic;
    font-weight: 300;
    font-size: 34px;
    color: var(--ink-light);
  }
  .back__bear {
    position: absolute;
    left: 145px; top: 145px;
    width: 165px; height: 155px;
    background: radial-gradient(ellipse 60% 60% at 50% 45%, var(--fur-light) 0%, var(--fur-dark) 70%, rgba(74, 42, 20, 0) 100%);
  }
  .contact {
    position: absolute;
    left: 436px; top: 148px;
    list-style: none;
    font-family: "Open Sans", sans-serif;
    font-size: 25px;
    color: var(--ink-light);
  }
  .contact__item { display: flex; align-items: center; height: 35px; }
  .contact__icon { width: 22px; height: 22px; margin-right: 31px; flex: none; }
  .back__wordmark {
    position: absolute;
    left: 0; top: 355px;
    width: 100%;
    text-align: center;
    font-family: "Bangers", sans-serif;
    font-size: 64px;
    letter-spacing: 5px;
    color: var(--ember);
    text-transform: uppercase;
  }
</style>
</head>
<body>
<div class="canvas">

  <section class="card card--front">
    <div class="front__wordmark"><span>Feral</span><span>Horizon</span></div>
    <div class="front__bear" role="img" aria-label="Photo of a roaring grizzly bear"></div>
    <svg class="front__target" viewBox="0 0 144 170" aria-hidden="true">
      <g fill="none" stroke="var(--target)" stroke-width="2.5">
        <circle cx="72" cy="85" r="55"/>
        <circle cx="72" cy="85" r="38"/>
        <circle cx="72" cy="85" r="20"/>
        <circle cx="72" cy="85" r="6"/>
        <line x1="2" y1="85" x2="142" y2="85"/>
        <line x1="72" y1="2" x2="72" y2="168"/>
      </g>
    </svg>
  </section>

  <section class="card card--back">
    <div class="back__band"></div>
    <h1 class="back__name">Corwin Aldersby</h1>
    <p class="back__role">Lead Developer</p>
    <div class="back__bear" role="img" aria-label="Photo of a roaring grizzly bear"></div>
    <ul class="contact">
      <li class="contact__item">
        <svg class="contact__icon" viewBox="0 0 22 22" aria-hidden="true">
          <circle cx="11" cy="11" r="11" fill="var(--ink-light)"/>
          <g fill="none" stroke="var(--bark)" stroke-width="1">
            <circle cx="11" cy="11" r="5"/>
            <ellipse cx="11" cy="11" rx="2.2" ry="5"/>
            <line x1="6" y1="11" x2="16" y2="11"/>
          </g>
        </svg>
        www.FeralHorizon.example
      </li>
      <li class="contact__item">
        <svg class="contact__icon" viewBox="0 0 22 22" aria-hidden="true">
          <circle cx="11" cy="11" r="11" fill="var(--ink-light)"/>
          <rect x="5.5" y="7" width="11" height="8" fill="var(--bark)"/>
          <polyline points="5.5,7 11,11.5 16.5,7" fill="none" stroke="var(--ink-light)" stroke-width="1"/>
        </svg>
        Pale_Lanterns@mailbox.example
      </li>
      <li class="contact__item">
        <svg class="contact__icon" viewBox="0 0 22 22" aria-hidden="true">
          <circle cx="11" cy="11" r="11" fill="var(--ink-light)"/>
          <rect x="7.5" y="5" width="7" height="12" rx="1.5" fill="var(--bark)"/>
          <rect x="8.8" y="6.6" width="4.4" height="7.5" fill="var(--ink-light)"/>
        </svg>
        555-207-3186
      </li>
    </ul>
    <div class="back__wordmark">Feral Horizon</div>
  </section>

</div>
</body>
</html>
```